New Business Card for Casual Beachfront Cafe

Quirky Beachfront Cafe at Moana, South Australia needs a DOUBLE SIDED business card to print on PrintHarbor.

Target Market(s)

Business Cards sit on the counter for Guests to take with them. Please view our website www.saltreefcafe.com.au to get a feel for the Cafe. You may also view our Instagram at @saltreefcafe

Industry/Entity Type

Cafe / Restaurant

Contact Information for Business Card

Information equivalent to: Breakfast, Lunch, Dinner, Coffee, Takeaway / 117 Parade Tidewater SA 5990 / Menu & Opening Hours: www.saltreefcafe.com.au / ph (08) 8461 9273

Requirements
Must have
• Information equivalent to: Breakfast, Lunch, Dinner, Coffee, Takeaway / 117 Parade Tidewater SA 5990 / Menu & Opening Hours: www.saltreefcafe.com.au / ph (08) 8461 9273
Nice to have
• Potentially some of our trademark colours (Cafe can be searched via Seekly)
Should not have
• Must NOT have image of the building. May have the logo provided on one side but not necessarily, depending on how you wish to design the card

```html
<!DOCTYPE html>
<html lang="en">
<head>
<meta charset="utf-8">
<title>Salt Reef Cafe – Business Card</title>
<link href="https://fonts.googleapis.com/css2?family=Montserrat:wght@400;500;700;800;900&family=Saira+Condensed:wght@700&display=swap" rel="stylesheet">
<style>
  :root{
    --stage:#e4e4e2;
    --rust:#c4661e;
    --navy:#1f5390;
    --sun:#f1c232;
    --coral:#ea7d5d;
    --teal:#17c08f;
    --paper:#ffffff;
    --frame:#e8a56f;
  }
  *{margin:0;padding:0;box-sizing:border-box}
  html,body{width:1200px;height:900px;overflow:hidden;background:var(--stage)}
  .stage{width:1200px;height:900px;display:flex;align-items:center;justify-content:center;gap:40px}
  .card{position:relative;width:540px;height:309px;border-radius:18px;overflow:hidden;box-shadow:0 10px 28px rgba(0,0,0,.18)}

  /* Front */
  .card--front{background:var(--rust)}
  .brand-frame{position:absolute;left:150px;top:52px;width:240px;height:120px;border:1px solid var(--frame);display:flex;align-items:center;justify-content:center}
  .brand-name{font-family:"Montserrat",sans-serif;font-weight:900;font-size:34px;line-height:1.02;color:var(--sun);text-align:center;letter-spacing:.5px;text-transform:uppercase}
  .services{position:absolute;left:0;right:0;top:212px;text-align:center;font-family:"Saira Condensed",sans-serif;font-weight:700;font-size:17px;letter-spacing:2.2px;color:var(--paper)}
  .services .sep{margin:0 9px}
  .colour-band{position:absolute;left:0;bottom:0;width:540px;height:24px;background:linear-gradient(90deg,var(--sun),var(--coral) 50%,var(--teal))}

  /* Back */
  .card--back{background:var(--paper)}
  .card--back .brand-name{position:absolute;left:0;right:0;top:30px;color:var(--navy);font-size:32px}
  .name-bar{position:absolute;left:28px;top:132px;width:484px;height:36px;background:var(--teal)}
  .person{position:absolute;left:0;right:0;top:134px;text-align:center;font-family:"Montserrat",sans-serif;font-weight:900;font-size:27px;letter-spacing:1px;color:var(--paper);text-transform:uppercase}
  .role{position:absolute;left:0;right:0;top:176px;text-align:center;font-family:"Montserrat",sans-serif;font-weight:400;font-size:14px;color:var(--navy)}
  .phone{position:absolute;left:0;right:0;top:204px;text-align:center;font-family:"Montserrat",sans-serif;font-weight:700;font-size:27px;color:var(--navy);letter-spacing:.5px}
  .details{position:absolute;left:0;right:0;top:250px;text-align:center;font-family:"Montserrat",sans-serif;font-weight:500;font-size:13px;color:var(--navy)}
  .details .sep{margin:0 8px}
  .details .web{font-weight:700}
</style>
</head>
<body>
<main class="stage">

  <section class="card card--front" aria-label="Card front">
    <div class="brand-frame">
      <p class="brand-name">Salt Reef<br>Cafe</p>
    </div>
    <p class="services">BREAKFAST<span class="sep">|</span>LUNCH<span class="sep">|</span>DINNER<span class="sep">|</span>COFFEE<span class="sep">|</span>TAKEAWAY</p>
    <div class="colour-band" role="img" aria-label="Decorative multicolour band in yellow, coral and teal"></div>
  </section>

  <section class="card card--back" aria-label="Card back">
    <p class="brand-name">Salt Reef<br>Cafe</p>
    <div class="name-bar" role="img" aria-label="Decorative colour stripe behind the name"></div>
    <p class="person">Rowan Keller</p>
    <p class="role">Owner/CEO</p>
    <p class="phone">(08) 8461 9273</p>
    <p class="details">117 Parade Tidewater SA 5990<span class="sep">|</span><span class="web">saltreefcafe</span>.com.au</p>
  </section>

</main>
</body>
</html>
```